Tidewell building company Business card design

I need a business card design for my company. I have a logo but dont have business cards with our logo..

www.tidewellbuildingco.com.au

The logo is on the website

I need the same details as this design I have attached. we have changed the logo and colours. just like the website

```html
<!DOCTYPE html>
<html lang="en">
<head>
<meta charset="utf-8">
<title>Tidewell Building – Business Card</title>
<link rel="stylesheet" href="https://fonts.googleapis.com/css2?family=Cinzel:wght@400&family=Open+Sans:wght@400;600&display=swap">
<style>
  :root {
    --stage: #e9e7e3;
    --card-white: #ffffff;
    --ink: #3a3a3a;
    --ink-soft: #555555;
    --accent: #3fa9d6;
    --dark-band: #1f2124;
    --dark-card: #17181a;
    --dark-card-edge: #2a2c2f;
    --band-text: #c9c9c9;
  }
  * { box-sizing: border-box; margin: 0; padding: 0; }
  html, body { width: 1200px; height: 1023px; overflow: hidden; }
  body {
    background: var(--stage);
    font-family: "Open Sans", Arial, sans-serif;
    position: relative;
  }
  .card {
    position: absolute;
    width: 525px;
    height: 300px;
    border-radius: 3px;
    box-shadow: 0 6px 18px rgba(0,0,0,0.18);
    overflow: hidden;
  }
  /* Front */
  .card-front { left: 70px; top: 130px; background: var(--card-white); }
  .card-front .accent-line {
    position: absolute; left: 0; right: 0; bottom: 58px; height: 6px;
    background: var(--accent);
  }
  .card-front .dark-band {
    position: absolute; left: 0; right: 0; bottom: 0; height: 58px;
    background: var(--dark-band);
  }
  .reg-number {
    position: absolute; right: 24px; bottom: 20px;
    font-size: 12px; color: var(--band-text); letter-spacing: 0.5px;
  }
  .brand {
    position: absolute; left: 34px; top: 100px;
    display: flex; align-items: center; gap: 12px;
  }
  .brand-square { width: 26px; height: 26px; background: var(--accent); }
  .brand-name {
    font-family: "Open Sans", Arial, sans-serif;
    font-weight: 600; font-size: 22px; line-height: 1.1;
    color: var(--accent); letter-spacing: 2px; text-transform: uppercase;
  }
  .person {
    position: absolute; right: 26px; top: 24px; text-align: right;
  }
  .person-name {
    font-family: "Cinzel", Georgia, serif;
    font-size: 21px; color: var(--ink); letter-spacing: 1.5px;
  }
  .person-title { font-size: 12px; color: var(--accent); margin-top: 2px; }
  .contacts {
    position: absolute; right: 26px; top: 88px;
    list-style: none; text-align: right;
    font-size: 11.5px; color: var(--ink-soft); line-height: 17px;
  }
  .contacts li { display: flex; justify-content: flex-end; align-items: center; gap: 8px; }
  .contacts svg { width: 11px; height: 11px; flex: none; }
  .address {
    position: absolute; right: 26px; top: 186px; text-align: right;
    font-style: normal; font-size: 11.5px; color: var(--ink-soft); line-height: 17px;
  }
  /* Back */
  .card-back {
    left: 605px; top: 593px;
    background: linear-gradient(160deg, var(--dark-card-edge) 0%, var(--dark-card) 45%, var(--dark-card) 100%);
    display: flex; align-items: center; justify-content: center;
  }
  .tagline { font-size: 15px; color: var(--accent); letter-spacing: 0.5px; }
</style>
</head>
<body>
  <section class="card card-front" aria-label="Business card front">
    <div class="brand">
      <span class="brand-square"></span>
      <span class="brand-name">Tidewell<br>Building</span>
    </div>

    <div class="person">
      <p class="person-name">Marek Dalton</p>
      <p class="person-title">Director</p>
    </div>

    <ul class="contacts">
      <li>08 9400 1850
        <svg viewBox="0 0 11 11"><rect width="11" height="11" rx="1.5" fill="var(--accent)"/><path d="M3 2.5l1.3 0 .6 1.6-.8.6a4.5 4.5 0 0 0 2.2 2.2l.6-.8 1.6.6v1.3c-3 .3-5.8-2.5-5.5-5.5z" fill="#fff"/></svg></li>
      <li>08 9400 1851
        <svg viewBox="0 0 11 11"><rect width="11" height="11" rx="1.5" fill="var(--accent)"/><rect x="3" y="2.5" width="5" height="6" fill="#fff"/></svg></li>
      <li>0412 555 019
        <svg viewBox="0 0 11 11"><rect width="11" height="11" rx="1.5" fill="var(--accent)"/><rect x="3.8" y="2" width="3.4" height="7" rx="0.6" fill="#fff"/></svg></li>
      <li>tidewellbuildingco@mailbox.com
        <svg viewBox="0 0 11 11"><rect width="11" height="11" rx="1.5" fill="var(--accent)"/><rect x="2.2" y="3.2" width="6.6" height="4.6" fill="#fff"/><path d="M2.2 3.2l3.3 2.6 3.3-2.6" stroke="var(--accent)" stroke-width="0.8" fill="none"/></svg></li>
      <li>www.tidewellbuildingco.com.au
        <svg viewBox="0 0 11 11"><rect width="11" height="11" rx="1.5" fill="var(--accent)"/><circle cx="5.5" cy="5.5" r="3" fill="none" stroke="#fff" stroke-width="0.9"/><path d="M2.5 5.5h6" stroke="#fff" stroke-width="0.8"/></svg></li>
    </ul>

    <address class="address">
      Unit 1 Level 1,<br>
      27 Coralbay Ave,<br>
      Westmere, WA 6041
    </address>

    <div class="accent-line"></div>
    <div class="dark-band"><span class="reg-number">Reg. No. 20913</span></div>
  </section>

  <section class="card card-back" aria-label="Business card back">
    <p class="tagline">We Build Unique And Beautiful Homes</p>
  </section>
</body>
</html>
```